Velliora Events Business Card

We need a business cards that stands out to our clients. We are company who targets prestige clients to spend money with us on experiences, so our image needs to be prestige
Target Market(s)
Corporate
Contact Information for Business Card
There will be four different names on the business cards
Danielle Brontoss
Director
O: 02 5174 2038
M: 0491 652 083
E: info@vellioraevents.example.com.au
Facebook: @vellioraevents
Instagram: vellioraevents
www.vellioraevents.example.com.au
Nathaniel Brontoss
Director
O: 02 5174 2038
M: 0478 205 946
Facebook: @vellioraevents
Instagram: vellioraevents
www.vellioraevents.example.com.au
Elias Dorvek
Director
O: 02 5174 2038
M: 0467 319 752
Facebook: @vellioraevents
Instagram: vellioraevents
www.vellioraevents.example.com.au
Marta Quell
Director
O: 02 5174 2038
Facebook: @vellioraevents
Instagram: vellioraevents
www.vellioraevents.example.com.au
Colors
Designer to choose colors to be used in the design.
Look and feel

```html
<!DOCTYPE html>
<html lang="en">
<head>
<meta charset="utf-8">
<title>Velliora Events Business Card</title>
<link rel="stylesheet" href="https://fonts.googleapis.com/css2?family=Tinos:wght@400;700&display=swap">
<style>
  :root {
    --card-ink: #2a2352;
    --card-ink-deep: #241d47;
    --gold: #d6a63a;
    --gold-light: #f1cf6b;
    --paper-white: #f4f2f8;
    --backdrop-top: #e9ebee;
    --backdrop-bottom: #b9bcc1;
  }
  * { box-sizing: border-box; margin: 0; padding: 0; }
  html, body { width: 1200px; height: 800px; overflow: hidden; }
  body {
    background: linear-gradient(160deg, var(--backdrop-top), var(--backdrop-bottom));
    font-family: "Tinos", "Times New Roman", serif;
    position: relative;
  }
  .card {
    position: absolute;
    width: 620px;
    height: 344px;
    background: linear-gradient(135deg, var(--card-ink), var(--card-ink-deep));
    box-shadow: 0 6px 18px rgba(0,0,0,0.28);
  }
  .card--front { left: 420px; top: 40px; }
  .card--back { left: 160px; top: 416px; }

  /* Front */
  .front-brand {
    position: absolute;
    left: 0; right: 0; top: 120px;
    display: flex; flex-direction: column; align-items: center; gap: 22px;
  }
  .brand-dot {
    width: 34px; height: 34px; border-radius: 50%;
    border: 2px solid var(--gold);
  }
  .brand-name {
    color: var(--gold);
    font-weight: 400;
    font-size: 30px;
    letter-spacing: 9px;
    text-transform: uppercase;
    white-space: nowrap;
  }

  /* Back */
  .back-brand {
    position: absolute;
    left: 0; width: 300px; top: 0; bottom: 0;
    display: flex; flex-direction: column; align-items: center; justify-content: center; gap: 18px;
  }
  .back-brand .brand-name { font-size: 19px; letter-spacing: 4px; }
  .divider {
    position: absolute;
    left: 300px; top: 90px;
    width: 1.5px; height: 160px;
    background: linear-gradient(to bottom, transparent, var(--gold) 20%, var(--gold) 80%, transparent);
  }
  .contact {
    position: absolute;
    left: 332px; top: 96px;
    color: var(--paper-white);
  }
  .contact-name {
    color: var(--gold);
    font-weight: 700;
    font-size: 20px;
    line-height: 1;
  }
  .contact-role { font-size: 15px; margin-top: 4px; }
  .contact-list { list-style: none; margin-top: 18px; }
  .contact-list li {
    display: flex; align-items: center; gap: 8px;
    font-size: 16px; line-height: 21px;
    white-space: nowrap;
  }
  .contact-icon { width: 12px; height: 12px; flex: none; }
  .contact-icon--plain { background: var(--gold); border-radius: 2px; }
</style>
</head>
<body>
  <section class="card card--front" aria-label="Card front">
    <div class="front-brand">
      <span class="brand-dot"></span>
      <span class="brand-name">Velliora Events</span>
    </div>
  </section>

  <section class="card card--back" aria-label="Card back">
    <div class="back-brand">
      <span class="brand-dot"></span>
      <span class="brand-name">Velliora Events</span>
    </div>
    <div class="divider"></div>
    <div class="contact">
      <p class="contact-name">Danielle Brontoss</p>
      <p class="contact-role">Director</p>
      <ul class="contact-list">
        <li>
          <svg class="contact-icon" viewBox="0 0 12 12"><rect x="3" y="0.7" width="6" height="10.6" rx="1" fill="none" stroke="#d6a63a" stroke-width="1.2"/><line x1="5" y1="9.4" x2="7" y2="9.4" stroke="#d6a63a" stroke-width="1"/></svg>
          0491 652 083
        </li>
        <li>
          <svg class="contact-icon" viewBox="0 0 12 12"><rect x="0.7" y="2.2" width="10.6" height="7.6" fill="none" stroke="#d6a63a" stroke-width="1.2"/><polyline points="0.7,2.4 6,6.6 11.3,2.4" fill="none" stroke="#d6a63a" stroke-width="1.2"/></svg>
          info@vellioraevents.example.com.au
        </li>
        <li><span class="contact-icon contact-icon--plain"></span>/vellioraevents</li>
        <li><span class="contact-icon contact-icon--plain"></span>@vellioraevents</li>
        <li>
          <svg class="contact-icon" viewBox="0 0 12 12"><circle cx="6" cy="6" r="5.2" fill="none" stroke="#d6a63a" stroke-width="1.1"/><ellipse cx="6" cy="6" rx="2.3" ry="5.2" fill="none" stroke="#d6a63a" stroke-width="1"/><line x1="0.8" y1="6" x2="11.2" y2="6" stroke="#d6a63a" stroke-width="1"/></svg>
          www.vellioraevents.example.com.au
        </li>
      </ul>
    </div>
  </section>
</body>
</html>
```